Business Card Design Project

Design is for the business card of a holistic, integral therapist. Design is required for front (colour / pattern) and back (white, with text as below).

Please prepare the design using placeholder text. I will work with the winning submission to complete the final information in the last iteration.

To give you a sense of her services a profile is below:
- I offer an integrative approach for effective relief of many issues such as anxiety, panic attacks, relationship difficulties, and health problems. In my counselling sessions I mainly use QBR {Quiet Balance Release } which taps into the body's energy system (meridians) to clear up blockages and limiting /distorted thinking and beliefs. I also work on expanding awareness as well as enhancing relationships.Clients have found the sessions life changing and report feeling lighter, clearer more empowered and connected to themselves and others.

Target Market(s)

Well educated, upper socioeconomic people seeking purpose and happiness in their lives.

Industry/Entity Type

Health

Requirements
Must have
• Must have the following text on front

First Name, Last Name
LLB, ND, Dip C
Counselling & Naturopathy
Quiet Balnce Release and Marlow Therapy

Adress 1 Line 1
Adress 1 Line 2

Adress 2 Line 1
Adress 2 Line 2

xxx.xxx@xxxxx.com

Tel: 0XXX XXX XXX

Must have the following text on reverse - which should be primarily white.

Next appointment
Date:
Time:
Nice to have
• Example colour palettes

http://www.huebinder.example/swatch/512093/velvet_lantern
http://www.huebinder.example/swatch/318420/Quiet_Orchard
http://www.huebinder.example/swatch/607215/Morning_Over_Tides

Example images that may be useful...
http://www.shopvarn.example/gp/product/images/4719205536/ref=dp_image_text_0?ie=UTF8&n=517302&s=books
http://www.shopvarn.example/gp/customer-media/product-gallery/6284019573/ref=cm_ciu_pdp_images_all
http://en.loreweb.example/wiki/File:Lotus_Grid_256bw.gif

```html
<!DOCTYPE html>
<html lang="en">
<head>
<meta charset="utf-8">
<title>Business Card – Front and Back</title>
<link rel="stylesheet" href="https://fonts.googleapis.com/css2?family=Marcellus+SC&family=Arimo&display=swap">
<style>
  :root {
    --page: #ffffff;
    --ink: #111111;
    --card-edge: #3a3a3a;
    --line-green: #7cc63a;
    --line-green-soft: rgba(124, 198, 58, 0.45);
    --front-text: #fdfbf6;
    --front-shadow: #5a1f1f;
    --bg-sky: #b9d6e6;
    --bg-mist: #d8ead2;
    --bg-meadow: #c3e0a8;
    --bg-warm: #cfc7a8;
  }
  * { box-sizing: border-box; margin: 0; padding: 0; }
  html, body { width: 1200px; height: 508px; overflow: hidden; background: var(--page); }
  .canvas { position: relative; width: 1200px; height: 508px; }

  .card {
    position: absolute;
    top: 72px;
    width: 487px;
    height: 292px;
    border: 1.5px solid var(--card-edge);
    overflow: hidden;
    font-family: "Marcellus SC", serif;
  }
  .card--front { left: 63px; }
  .card--back { left: 663px; background: var(--page); }

  .front-backdrop {
    position: absolute; inset: 0;
    background:
      radial-gradient(ellipse at 62% 45%, var(--bg-warm) 0%, transparent 45%),
      linear-gradient(160deg, var(--bg-sky) 0%, var(--bg-mist) 50%, var(--bg-meadow) 100%);
  }
  .accent-rule { position: absolute; background: var(--line-green); }
  .accent-rule--top { left: 8px; top: 13px; width: 462px; height: 2px;
    background: linear-gradient(90deg, var(--line-green) 70%, transparent); }
  .accent-rule--top-soft { left: 8px; top: 17px; width: 430px; height: 1px; background: var(--line-green-soft); }
  .accent-rule--side { left: 22px; top: 5px; width: 2px; height: 270px;
    background: linear-gradient(180deg, var(--line-green) 60%, transparent); }
  .accent-rule--side-soft { left: 26px; top: 5px; width: 1px; height: 240px; background: var(--line-green-soft); }

  .front-text {
    position: absolute;
    color: var(--front-text);
    font-size: 14px;
    line-height: 20px;
    text-shadow: 1px 1px 1px var(--front-shadow), 0 0 2px var(--front-shadow);
    white-space: nowrap;
  }
  .services { right: 25px; top: 26px; text-align: right; line-height: 22px; }
  .address { right: 25px; text-align: right; }
  .address--first { top: 76px; }
  .address--second { top: 139px; }
  .identity { left: 50px; top: 158px; line-height: 22px; }
  .contact { left: 50px; top: 220px; line-height: 21px; }

  .appointment-title {
    position: absolute; left: 29px; top: 19px;
    font-size: 17px; color: var(--ink);
    border-bottom: 1.5px solid var(--ink);
    line-height: 18px;
  }
  .appointment-table {
    position: absolute; left: 29px; top: 50px;
    width: 424px; border-collapse: collapse;
    table-layout: fixed;
  }
  .appointment-table th, .appointment-table td {
    border: 1.5px solid var(--ink);
    height: 26px;
  }
  .appointment-table th {
    font-weight: normal; font-size: 15px; color: var(--ink);
    text-align: center;
  }

  .side-label {
    position: absolute; top: 392px;
    font-family: "Arimo", sans-serif;
    font-size: 48px; color: var(--ink);
    transform: translateX(-50%);
  }
  .side-label--front { left: 308px; }
  .side-label--back { left: 905px; }
</style>
</head>
<body>
<main class="canvas">
  <section class="card card--front">
    <div class="front-backdrop" role="img" aria-label="Soft, hazy photograph of a fairground wheel against a pale sky"></div>
    <span class="accent-rule accent-rule--top"></span>
    <span class="accent-rule accent-rule--top-soft"></span>
    <span class="accent-rule accent-rule--side"></span>
    <span class="accent-rule accent-rule--side-soft"></span>

    <p class="front-text services">Quiet Balnce Release and Marlow Therapy,<br>Counselling &amp; Naturopathy</p>
    <p class="front-text address address--first">Adress 1 Line 1<br>Adress 1 Line 2</p>
    <p class="front-text address address--second">Adress 2 Line 1<br>Adress 2 Line 2</p>
    <p class="front-text identity">First Name, Last Name<br>LLB, ND, Dip C.</p>
    <p class="front-text contact">xxx.xxx@xxxxx.com<br>Tel: 0XXX XXX XXX</p>
  </section>

  <section class="card card--back">
    <h2 class="appointment-title" style="font-weight:normal">Next Appointment</h2>
    <table class="appointment-table">
      <colgroup>
        <col style="width:82px"><col style="width:129px"><col style="width:86px"><col style="width:127px">
      </colgroup>
      <thead>
        <tr><th>Date</th><th>Time</th><th>Date</th><th>Time</th></tr>
      </thead>
      <tbody>
        <tr><td></td><td></td><td></td><td></td></tr>
        <tr><td></td><td></td><td></td><td></td></tr>
        <tr><td></td><td></td><td></td><td></td></tr>
        <tr><td></td><td></td><td></td><td></td></tr>
        <tr><td></td><td></td><td></td><td></td></tr>
        <tr><td></td><td></td><td></td><td></td></tr>
        <tr><td></td><td></td><td></td><td></td></tr>
      </tbody>
    </table>
  </section>

  <p class="side-label side-label--front">FRONT</p>
  <p class="side-label side-label--back">BACK</p>
</main>
</body>
</html>
```